Meridian Dash add on sales tool2017

This will be a flyer to leave with our clients we just did work for. We want to entice them to use our other services over the next 30 days with a discount, money off etc. we will write in the special and the expiration date. I want the client to read the description and see a picture of the service they may want done.

Target Market(s)

Repeat clients

Industry/Entity Type

Cleaning Service

Font styles to use
Serif
Sans Serif

Colors
ec1f27
000000
b1b1b1

Requirements
Must have
• Call to action! look high end market, clients show we do 1st class work.
• Don't Waite
Nice to have
• Classy, quality, I'm open to using other pictures that may look better
Should not have
• Look like a typical carpet cleaners special flyer
• Not to look cluttered

```html
<!DOCTYPE html>
<html lang="en">
<head>
<meta charset="utf-8">
<title>Meridian Dash – 30 Day Special Offer</title>
<link rel="stylesheet" href="https://fonts.googleapis.com/css2?family=Open+Sans:wght@400;600;700;800&family=Roboto+Condensed:wght@700&display=swap">
<style>
  :root{
    --red:#ec1f27;
    --red-deep:#b5121a;
    --black:#000000;
    --ink:#141414;
    --grey:#b1b1b1;
    --white:#ffffff;
  }
  *{margin:0;padding:0;box-sizing:border-box}
  html,body{width:1041px;height:1200px;overflow:hidden;background:var(--black)}
  body{font-family:"Open Sans",Arial,sans-serif;color:var(--white)}
  .flyer{position:relative;width:1041px;height:1200px;overflow:hidden;background:var(--black)}

  /* header */
  .brand-box{position:absolute;left:0;top:0;width:387px;height:194px;
    background:radial-gradient(ellipse at 45% 40%,#3a3a3a 0%,#1a1a1a 55%,#050505 100%);
    display:flex;align-items:center;justify-content:center;padding-top:20px}
  .brand-name{font-family:"Open Sans",Arial,sans-serif;font-weight:700;font-size:30px;color:var(--white);letter-spacing:.5px}

  .offer-area{position:absolute;left:387px;top:0;right:0;height:194px;background:var(--white)}
  .offer-tab{position:absolute;top:0;height:58px;background:var(--red)}
  .offer-tab.left{left:0;width:79px}
  .offer-tab.right{right:0;width:85px}
  .offer-banner{position:absolute;top:0;left:84px;width:478px;height:58px;
    background:linear-gradient(180deg,#2a2a2a,#0c0c0c);
    display:flex;align-items:center;justify-content:center;gap:12px}
  .offer-banner .lead{font-family:"Open Sans",Arial,sans-serif;font-weight:600;font-size:33px}
  .offer-banner .accent{font-family:"Roboto Condensed",Arial,sans-serif;font-weight:700;font-size:36px;color:var(--red)}
  .expires{position:absolute;left:12px;bottom:6px;font-size:21px;font-weight:700;color:var(--ink)}

  /* call to action bar */
  .cta-bar{position:absolute;left:0;top:194px;width:1041px;height:60px;background:var(--red)}
  .cta-label{position:absolute;left:24px;top:0;height:60px;display:flex;align-items:center;
    font-family:"Roboto Condensed",Arial,sans-serif;font-weight:700;font-size:36px}
  .cta-phone{position:absolute;left:384px;top:0;width:334px;height:60px;background:var(--black);
    clip-path:polygon(0 0,95% 0,100% 50%,95% 100%,0 100%,4% 50%);
    display:flex;align-items:center;justify-content:center;
    font-family:"Roboto Condensed",Arial,sans-serif;font-weight:700;font-size:42px}
  .cta-address{position:absolute;left:730px;top:9px;display:flex;gap:7px;font-size:17px;font-weight:600;line-height:1.3}
  .cta-address svg{margin-top:3px;flex:none}

  /* body */
  .services{position:absolute;left:0;top:254px;width:1041px;height:946px;
    background:linear-gradient(90deg,#000 0%,#1a0304 30%,#7a0a10 55%,var(--red-deep) 75%,var(--red) 100%)}
  .room-scene{position:absolute;inset:0;
    background:radial-gradient(ellipse at 70% 30%,rgba(236,31,39,.35),transparent 60%),
               radial-gradient(ellipse at 60% 95%,rgba(150,10,15,.5),transparent 55%)}
  .services-heading{position:absolute;left:0;right:0;top:10px;text-align:center;
    font-family:"Roboto Condensed",Arial,sans-serif;font-weight:700;font-size:33px}
  .heading-rule{position:absolute;left:99px;right:100px;top:55px;height:1px;background:var(--white)}
  .heading-rule::after{content:"";position:absolute;left:30%;width:35%;top:-1px;height:3px;background:var(--white)}

  .service{position:absolute;left:61px;width:500px}
  .service-title{font-weight:800;font-size:28px;line-height:1.1;text-transform:uppercase;display:inline-block;
    padding-bottom:4px;border-bottom:1px solid var(--white);position:relative}
  .service-title::after{content:"";position:absolute;left:0;bottom:-2px;width:38%;height:3px;background:var(--red)}
  .service-title .accent{color:var(--red)}
  .service-text{margin-top:8px;font-size:18px;line-height:23px}

  .service-photo{position:absolute;left:669px;width:313px;height:151px;border:4px solid #f1f1f1;box-shadow:0 2px 6px rgba(0,0,0,.5)}
  .photo-stairs{background:linear-gradient(160deg,#f2f2f2 0%,#d9d4cc 45%,#9a8f80 75%,#3a3a3a 100%)}
  .photo-upholstery{background:linear-gradient(90deg,#8e8b78 0%,#b6b29f 40%,#d9e3e2 55%,#7a3a30 100%);display:flex;align-items:flex-end;justify-content:space-between;padding:0 12px 2px 24px}
  .photo-upholstery span{background:var(--white);color:#1b2c7a;font-weight:700;font-size:15px;padding:0 8px;border:1px solid #1b2c7a}
  .photo-drapery{background:linear-gradient(90deg,#6b5a52 0%,#a99a90 25%,#202020 50%,#cfd6dc 70%,#7e6f66 100%)}
  .photo-tile{background:linear-gradient(120deg,#6f6a66 0%,#8c8782 40%,#c9bfb0 60%,#b8ad9c 100%)}
  .photo-stone{background:linear-gradient(180deg,#e7e7e7 0%,#bfc2c3 35%,#6d6e6c 70%,#9a9c9a 100%)}
</style>
</head>
<body>
<div class="flyer">

  <header>
    <div class="brand-box">
      <div class="brand-name">Meridian Dash</div>
    </div>
    <div class="offer-area">
      <div class="offer-tab left"></div>
      <div class="offer-banner"><span class="lead">30 DAY</span><span class="accent">SPECIAL OFFER!</span></div>
      <div class="offer-tab right"></div>
      <div class="expires">Expires</div>
    </div>
  </header>

  <div class="cta-bar">
    <div class="cta-label">CALL NOW TO BOOK</div>
    <div class="cta-phone">702 555-0148</div>
    <div class="cta-address">
      <svg width="12" height="16" viewBox="0 0 12 16" aria-hidden="true"><path d="M6 0C2.7 0 0 2.6 0 5.9 0 10.3 6 16 6 16s6-5.7 6-10.1C12 2.6 9.3 0 6 0zm0 8.2a2.3 2.3 0 1 1 0-4.6 2.3 2.3 0 0 1 0 4.6z" fill="#fff"/></svg>
      <div>1480 W. Juniper Ave. Suite B<br>702 555-0148 Las Vegas</div>
    </div>
  </div>

  <main class="services">
    <div class="room-scene" role="img" aria-label="Elegant living room with arched windows and an oriental rug, tinted red"></div>
    <h1 class="services-heading">ONE STOP FOR ALL YOUR HOME CLEANING NEEDS</h1>
    <div class="heading-rule"></div>

    <section class="service" style="top:74px">
      <h2 class="service-title">Carpet <span class="accent">Cleaning</span></h2>
      <p class="service-text">Don't let dirty carpets spoil the look of your beautiful home!. with 37 years of cleaning carpets experience you can expect your carpets to look like new in most cases.</p>
    </section>
    <div class="service-photo photo-stairs" style="top:79px" role="img" aria-label="Freshly cleaned carpeted staircase"></div>

    <section class="service" style="top:242px">
      <h2 class="service-title">Upholstery <span class="accent">Cleaning</span></h2>
      <p class="service-text">Every day use leaves your sofa's and chairs looking dingy and can smell like dog. Our Dry cleaning, Shampoo or Rinse extraction will leave the fabric feel like clean sheet!</p>
    </section>
    <div class="service-photo photo-upholstery" style="top:249px" role="img" aria-label="Before and after upholstery cleaning comparison"><span>Before</span><span>After</span></div>

    <section class="service" style="top:408px">
      <h2 class="service-title">Drapery <span class="accent">Cleaning</span></h2>
      <p class="service-text">Drapery's act like a filter attracting atmospheric soil! Making them look dingy, We make it easy to Dry clean in-home! Safe and effective beautiful drapery again.</p>
    </section>
    <div class="service-photo photo-drapery" style="top:416px" role="img" aria-label="Technician cleaning drapes in a home"></div>

    <section class="service" style="top:590px">
      <h2 class="service-title">Tile &amp; Grout <span class="accent">Cleaning</span></h2>
      <p class="service-text">Tile &amp; Grout get neglected! Dirty grout can leave permanent staining. Let our professionals bring back the look of a new floor.</p>
    </section>
    <div class="service-photo photo-tile" style="top:585px" role="img" aria-label="Stone tile floor half cleaned, half dirty"></div>

    <section class="service" style="top:752px">
      <h2 class="service-title">Natural Stone<br><span class="accent">Cleaning &amp; Polishing</span></h2>
      <p class="service-text">A dull stained Marble - Granite-Travertine and other Natural stone can be revitalized to look NEW again!</p>
    </section>
    <div class="service-photo photo-stone" style="top:753px" role="img" aria-label="Polished marble floor reflecting window light"></div>
  </main>

</div>
</body>
</html>
```